DL Flyer & Matching business card

I have done a mock DL flyer, i am happy with the back ground and layout. i need you to fix and format fonts so i looks better...i am happy for you to change icons and fonts but not the layout...i also want a business card to match,, with out all the text obviously but the same background as DL flyer so they match...

My colours are
Blue
PMS coated 2192c
PMS uncoated 2995u
CMYK C80: M10: Y0: K0
RGB R0: G163: B224
HEX #00A3E0

Grey/Black
PMS coated 7540C
PMS uncoated Cool grey 11U
CMYK C0: M0: Y0: K77
RGB R95: G96: B98
HEX #5F6062

Industry/Entity Type

Finance

Font styles to use
Sans Serif

Colors

Designer to choose colors to be used in the design.

Requirements
Must have
• my colours, i have the design, just need proper font formatting .
• Blue
• PMS coated 2192c
• PMS uncoated 2995u
• CMYK C80: M10: Y0: K0
• RGB R0: G163: B224
• HEX #00A3E0
• Grey/Black
• PMS coated 7540C
• PMS uncoated Cool grey 11U
• CMYK C0: M0: Y0: K77
• RGB R95: G96: B98
• HEX #5F6062

```html
<!DOCTYPE html>
<html lang="en">
<head>
<meta charset="utf-8">
<title>Northfield Lending Brokers – DL Flyer &amp; Business Card</title>
<link rel="stylesheet" href="https://fonts.googleapis.com/css2?family=Source+Sans+3:wght@300;400;600;700&display=swap">
<style>
  :root{
    --brand-blue:#00A3E0;
    --charcoal:#3d3c3d;
    --brand-grey:#5F6062;
    --board:#a0a0a0;
    --white:#ffffff;
    --paper:#ffffff;
    --font:"Source Sans 3", Arial, sans-serif;
  }
  *{box-sizing:border-box;margin:0;padding:0}
  html,body{width:1200px;height:1200px;overflow:hidden;background:var(--board)}
  body{font-family:var(--font)}
  .stage{position:absolute;left:0;top:0;width:1500px;height:1500px;transform:scale(.8);transform-origin:0 0}
  .label{position:absolute;color:var(--white);font-weight:400;font-size:47px;letter-spacing:.5px;transform:translateX(-50%);white-space:nowrap}
  .piece{position:absolute;overflow:hidden;box-shadow:0 2px 6px rgba(0,0,0,.35)}
  .piece svg.bg{position:absolute;left:0;top:0;width:100%;height:100%}
  .abs{position:absolute;white-space:nowrap}

  /* card front */
  .card-front{left:150px;top:241px;width:525px;height:374px;background:var(--brand-blue)}
  .card-front .wordmark{left:50%;top:50%;transform:translate(-50%,-50%);display:flex;align-items:center;gap:12px;color:var(--white);font-weight:600;font-size:24px;letter-spacing:.5px}
  .card-front .wordmark .square{width:18px;height:18px;background:var(--white)}

  /* card back */
  .card-back{left:780px;top:241px;width:525px;height:374px;background:var(--paper)}
  .brand-lockup{text-align:right;color:var(--brand-blue)}
  .brand-lockup .name{font-weight:600;line-height:1.05;letter-spacing:.3px}
  .brand-lockup .services{color:var(--charcoal);font-weight:400;line-height:1.5;text-align:center}
  .card-back .brand-lockup{right:22px;top:54px}
  .card-back .brand-lockup .name{font-size:22px}
  .card-back .brand-lockup .services{font-size:7px;margin-top:6px}
  .card-back .holder{left:26px;top:158px;color:var(--brand-blue);font-size:28px;font-weight:400;border-bottom:1.5px solid var(--brand-blue);line-height:1.15}
  .contact-list{list-style:none}
  .contact-list li{position:absolute;display:flex;align-items:center;white-space:nowrap}
  .contact-list svg{fill:var(--brand-blue)}
  .card-back .contact-list li{left:26px;color:var(--white);font-size:12.5px;gap:10px;height:16px}
  .card-back .contact-list svg{width:14px;height:14px}
  .card-back .contact-list .no-icon{padding-left:24px}

  /* flyer */
  .flyer{left:141px;top:790px;width:1217px;height:585px;background:var(--paper)}
  .flyer .headline{left:29px;top:76px;color:var(--white);font-weight:700;font-size:38px;letter-spacing:.3px}
  .benefit{position:absolute;left:34px;color:var(--white)}
  .benefit svg{position:absolute;left:0;top:3px;width:20px;height:20px;fill:var(--brand-blue)}
  .benefit h3{margin-left:34px;color:var(--brand-blue);font-weight:400;font-size:19px;line-height:22px}
  .benefit p{margin-left:34px;font-size:18px;line-height:21px;font-weight:400}
  .flyer .did-you-know{left:36px;top:406px;color:var(--brand-blue);font-weight:600;font-size:26px}
  .flyer .research{left:37px;top:450px;color:var(--white);font-size:17px;line-height:20px;white-space:normal;width:640px}
  .flyer .callout{left:37px;top:494px;color:var(--brand-blue);font-size:17px}
  .flyer .disclaimer{left:38px;top:533px;color:var(--white);font-size:10.5px}
  .flyer .brand-lockup{right:67px;top:88px}
  .flyer .brand-lockup .name{font-size:19px}
  .flyer .brand-lockup .services{font-size:5.6px;margin-top:5px}
  .flyer .lenders-title{left:644px;top:152px;font-size:24px;font-weight:600;color:var(--brand-blue);letter-spacing:.2px;padding-bottom:4px;border-bottom:1.5px solid var(--charcoal)}
  .flyer .lenders-title span{color:var(--charcoal)}
  .lender{position:absolute;transform:translateY(-50%);color:var(--charcoal);font-weight:600;font-size:15px;white-space:nowrap}
  .lender-badge{position:absolute;width:30px;height:30px;background:var(--brand-blue)}
  .flyer .contact-list li{color:var(--charcoal);font-size:17px;gap:12px;height:20px}
  .flyer .contact-list svg{width:18px;height:18px}
</style>
</head>
<body>
<main class="stage">

  <h2 class="label" style="left:418px;top:160px">Business card(front)</h2>
  <h2 class="label" style="left:1056px;top:160px">Business card(back)</h2>
  <h2 class="label" style="left:722px;top:712px">Flyer</h2>

  <!-- Business card front -->
  <section class="piece card-front">
    <div class="abs wordmark"><span class="square"></span>NORTHFIELD LENDING</div>
  </section>

  <!-- Business card back -->
  <section class="piece card-back">
    <svg class="bg" viewBox="0 0 525 374" preserveAspectRatio="none">
      <defs>
        <linearGradient id="interiorTone" x1="0" y1="0" x2="1" y2="1">
          <stop offset="0" stop-color="#ffffff"/>
          <stop offset=".6" stop-color="#f1f1f2"/>
          <stop offset="1" stop-color="#dcdcde"/>
        </linearGradient>
      </defs>
      <rect x="180" y="0" width="345" height="374" fill="url(#interiorTone)" role="img" aria-label="Faded photo of a bright living room interior"/>
      <polygon points="0,0 195,0 368,374 0,374" fill="var(--brand-blue)"/>
      <polygon points="0,0 178,0 348,374 0,374" fill="var(--charcoal)"/>
    </svg>

    <div class="abs brand-lockup">
      <div class="name">NORTHFIELD LENDING<br>BROKERS</div>
      <div class="services">HOME LOANS | PLANT &amp; EQUIPMENT | AUTOMOTIVE<br>BUSINESS &amp; COMMERCIAL | PERSONAL</div>
    </div>

    <div class="abs holder">Daniel Hartley</div>

    <ul class="contact-list">
      <li style="top:211px"><svg viewBox="0 0 24 24"><path d="M12 2a7 7 0 0 0-7 7c0 5 7 13 7 13s7-8 7-13a7 7 0 0 0-7-7zm0 9.5A2.5 2.5 0 1 1 12 6.5a2.5 2.5 0 0 1 0 5z"/></svg>8/22 Kestrel St Orange NSW 2800</li>
      <li style="top:240px"><svg viewBox="0 0 24 24"><path d="M6.6 10.8a15 15 0 0 0 6.6 6.6l2.2-2.2a1 1 0 0 1 1-.25 11.4 11.4 0 0 0 3.6.57 1 1 0 0 1 1 1V20a1 1 0 0 1-1 1A17 17 0 0 1 3 4a1 1 0 0 1 1-1h3.5a1 1 0 0 1 1 1 11.4 11.4 0 0 0 .57 3.6 1 1 0 0 1-.25 1z"/></svg>02 6100 0142</li>
      <li class="no-icon" style="top:269px">0400 555 218</li>
      <li style="top:298px"><svg viewBox="0 0 24 24"><path d="M2 5h20v14H2zm2 2v.5l8 5 8-5V7zm0 2.8V17h16V9.8l-8 5z"/></svg>daniel@northfieldlending.com.au</li>
      <li style="top:328px"><svg viewBox="0 0 24 24"><path d="M12 2a10 10 0 1 0 0 20 10 10 0 0 0 0-20zm6.9 6h-3a15.6 15.6 0 0 0-1.4-3.6A8 8 0 0 1 18.9 8zM12 4a14 14 0 0 1 1.9 4h-3.8A14 14 0 0 1 12 4zM4.3 14a8 8 0 0 1 0-4h3.4a16 16 0 0 0 0 4zm.8 2h3a15.6 15.6 0 0 0 1.4 3.6A8 8 0 0 1 5.1 16zm3-8h-3a8 8 0 0 1 4.4-3.6A15.6 15.6 0 0 0 8.1 8zM12 20a14 14 0 0 1-1.9-4h3.8A14 14 0 0 1 12 20zm2.3-6H9.7a14.7 14.7 0 0 1 0-4h4.6a14.7 14.7 0 0 1 0 4zm.2 5.6a15.6 15.6 0 0 0 1.4-3.6h3a8 8 0 0 1-4.4 3.6zm1.8-5.6a16 16 0 0 0 0-4h3.4a8 8 0 0 1 0 4z"/></svg>www.northfieldlending.com.au</li>
    </ul>
  </section>

  <!-- DL flyer -->
  <section class="piece flyer">
    <svg class="bg" viewBox="0 0 1217 585" preserveAspectRatio="none">
      <polygon points="0,0 530,0 802,585 0,585" fill="var(--brand-blue)"/>
      <polygon points="0,0 504,0 774,585 0,585" fill="var(--charcoal)"/>
      <polygon points="0,72 537,72 560,122 0,122" fill="var(--brand-blue)"/>
    </svg>

    <h1 class="abs headline">WHY USE A LOCAL BROKER</h1>

    <article class="benefit" style="top:142px">
      <svg viewBox="0 0 24 24"><path d="M5 2h14v2h-1v3a6 6 0 0 1-3.5 5 6 6 0 0 1 3.5 5v3h1v2H5v-2h1v-3a6 6 0 0 1 3.5-5A6 6 0 0 1 6 7V4H5zm3 2v3a4 4 0 0 0 8 0V4zm4 9a4 4 0 0 0-4 4v3h8v-3a4 4 0 0 0-4-4z"/></svg>
      <h3>SAVE TIME &amp; PRODUCT KNOWLEDGE</h3>
      <p>We will compare hundred of loans, including the big four<br>banks and a range of completive non-bank lenders to find you<br>the perfect solution for your personal financial needs.</p>
    </article>

    <article class="benefit" style="top:252px">
      <svg viewBox="0 0 24 24"><path d="M12 2a10 10 0 1 0 0 20 10 10 0 0 0 0-20zm0 18a8 8 0 1 1 0-16 8 8 0 0 1 0 16zm1-13h-2v6l5 3 1-1.7-4-2.3z"/></svg>
      <h3>CONVENIENCE</h3>
      <p>Unlike banks, we will arrange appointment out of normal hours<br>including Saturday mornings</p>
    </article>

    <article class="benefit" style="top:340px">
      <svg viewBox="0 0 24 24"><path d="M2 3h9l11 11-8 8L3 11zm4.5 2A1.5 1.5 0 1 0 6.5 8a1.5 1.5 0 0 0 0-3z"/></svg>
      <h3>IT'S FREE</h3>
      <p>You don't pay us a single cent! we are paid by the lender of your choice</p>
    </article>

    <h2 class="abs did-you-know">DID YOU KNOW?</h2>
    <p class="abs research">Recent research has found that brokers were responsible for more than 50% of mortgages in the last 12 months.</p>
    <p class="abs callout">Its seems everybody is realising the benefits of using a broker, have you?</p>
    <p class="abs disclaimer">Northfield Lending Brokers is a Credit Representative 520417 of Harbourline Broker Group Pty Ltd ACN 612 480 931, Australian Credit Licence 497260</p>

    <div class="abs brand-lockup">
      <div class="name">NORTHFIELD LENDING<br>BROKERS</div>
      <div class="services">HOME LOANS | PLANT &amp; EQUIPMENT | AUTOMOTIVE<br>BUSINESS &amp; COMMERCIAL | PERSONAL</div>
    </div>

    <h2 class="abs lenders-title">SOME OF OUR <span>LENDERS</span></h2>

    <div class="lenders">
      <span class="lender" style="left:672px;top:228px">Coastline Bank</span>
      <span class="lender" style="left:802px;top:228px">Ardent</span>
      <span class="lender" style="left:905px;top:226px">Meridian</span>
      <span class="lender" style="left:1008px;top:226px">Harbour Bank</span>
      <span class="lender-badge" style="left:1124px;top:204px"></span>

      <span class="lender" style="left:697px;top:277px">Eastgate Bank</span>
      <span class="lender" style="left:802px;top:277px">Southway</span>
      <span class="lender" style="left:898px;top:277px">Sunwest</span>
      <span class="lender" style="left:1034px;top:277px">Federal Lane Bank</span>

      <span class="lender" style="left:727px;top:326px">Homeway</span>
      <span class="lender" style="left:840px;top:326px">Keystone Direct</span>
      <span class="lender" style="left:989px;top:326px">Ridgeline</span>
      <span class="lender" style="left:1076px;top:326px">Summit</span>
      <span class="lender" style="left:1146px;top:326px">Acorn</span>
    </div>

    <ul class="contact-list">
      <li style="left:784px;top:413px"><svg viewBox="0 0 24 24"><path d="M12 2a7 7 0 0 0-7 7c0 5 7 13 7 13s7-8 7-13a7 7 0 0 0-7-7zm0 9.5A2.5 2.5 0 1 1 12 6.5a2.5 2.5 0 0 1 0 5z"/></svg>8/22 Kestrel St Orange NSW 2800</li>
      <li style="left:808px;top:442px"><svg viewBox="0 0 24 24"><path d="M6.6 10.8a15 15 0 0 0 6.6 6.6l2.2-2.2a1 1 0 0 1 1-.25 11.4 11.4 0 0 0 3.6.57 1 1 0 0 1 1 1V20a1 1 0 0 1-1 1A17 17 0 0 1 3 4a1 1 0 0 1 1-1h3.5a1 1 0 0 1 1 1 11.4 11.4 0 0 0 .57 3.6 1 1 0 0 1-.25 1z"/></svg>02 6100 0142</li>
      <li style="left:857px;top:471px">0400 555 218</li>
      <li style="left:844px;top:500px"><svg viewBox="0 0 24 24"><path d="M2 5h20v14H2zm2 2v.5l8 5 8-5V7zm0 2.8V17h16V9.8l-8 5z"/></svg>daniel@northfieldlending.com.au</li>
      <li style="left:865px;top:530px"><svg viewBox="0 0 24 24"><path d="M12 2a10 10 0 1 0 0 20 10 10 0 0 0 0-20zm6.9 6h-3a15.6 15.6 0 0 0-1.4-3.6A8 8 0 0 1 18.9 8zM12 4a14 14 0 0 1 1.9 4h-3.8A14 14 0 0 1 12 4zM4.3 14a8 8 0 0 1 0-4h3.4a16 16 0 0 0 0 4zm.8 2h3a15.6 15.6 0 0 0 1.4 3.6A8 8 0 0 1 5.1 16zm3-8h-3a8 8 0 0 1 4.4-3.6A15.6 15.6 0 0 0 8.1 8zM12 20a14 14 0 0 1-1.9-4h3.8A14 14 0 0 1 12 20zm2.3-6H9.7a14.7 14.7 0 0 1 0-4h4.6a14.7 14.7 0 0 1 0 4zm.2 5.6a15.6 15.6 0 0 0 1.4-3.6h3a8 8 0 0 1-4.4 3.6zm1.8-5.6a16 16 0 0 0 0-4h3.4a8 8 0 0 1 0 4z"/></svg>www.northfieldlending.com.au</li>
    </ul>
  </section>

</main>
</body>
</html>
```